A website for a Maltese Law Firm

Our law firm needs a website to further its business. The site should have a simple yet effective design. We would need the following sections: About us, Practice Areas, About Malta, Contact. These should be further split as follows:

About us: Our firm, Our values, What others say, Offices

Practice Areas: Crimimal, Citizenship & Residence, Overseas Patron Scheme, Criminal Defence, Civil Litigation, Arbitration and ADR, Commercial and Corporate, Media Law.

About Malta: just one section.

Contact: Just one section

We would also need a news feed at the front of the site to include latest news regarding our cases.

At the bottom we need a section for our Terms and a Privacy Statement.

Our logo is being attached.

Target Market(s)

All clients looking for legal assistance in Malta

Industry/Entity Type

Legal

Coding

Coded - Design and coding required

Number of Pages Required

1 page

Requirements
Must have
• It must be simple yet striking.

```html
<!DOCTYPE html>
<html lang="en">
<head>
<meta charset="utf-8">
<title>Mercieca &amp; Borg Advocates</title>
<link rel="stylesheet" href="https://fonts.googleapis.com/css2?family=Cinzel:wght@400;700&family=Open+Sans:ital,wght@0,400;0,600;1,400&display=swap">
<style>
:root{
  --blue:#0d47ec;
  --blue-dark:#0a39c4;
  --blue-soft:#3f73f2;
  --ink:#222;
  --muted:#555;
  --panel:#2c2c2e;
  --footer:#1c1c1d;
  --footer-bar:#111;
  --line:#d6d6d6;
  --cyan:#6fd0e0;
  --white:#fff;
}
*{box-sizing:border-box;margin:0;padding:0}
html,body{width:1200px;height:3564px;overflow:hidden}
body{font-family:"Open Sans",Arial,sans-serif;color:var(--ink);background:var(--white);font-size:13px;line-height:1.5}

/* header */
.site-header{height:114px;position:relative;border-top:3px solid var(--blue)}
.brand{position:absolute;left:80px;top:30px;text-align:center;font-family:"Cinzel",Georgia,serif;font-weight:700;color:#111;white-space:nowrap}
.brand-name{font-size:31px;line-height:1;letter-spacing:.3px}
.brand-tag{font-size:12px;letter-spacing:6px;line-height:14px;margin-top:6px}
.contact-col{position:absolute;top:16px;font-family:"Cinzel",Georgia,serif;font-size:13px;color:#222;line-height:18px}
.contact-col .row{display:flex;gap:10px;margin-bottom:12px}
.contact-col svg{flex:none;margin-top:2px}
.c1{left:604px}.c2{left:862px}

.main-nav{height:52px;background:var(--blue);display:flex;align-items:center;padding:0 58px}
.main-nav a{flex:1;text-align:center;color:var(--white);text-decoration:none;font-family:"Cinzel",Georgia,serif;font-size:17px;border-left:1px solid rgba(255,255,255,.35)}
.main-nav a:first-child{border-left:0;flex:.6;text-align:left;padding-left:22px}
.main-nav a:last-child{flex:.7;text-align:right}

/* hero */
.hero{height:549px;position:relative;background:linear-gradient(100deg,#8c8f96 0%,#c7c9cf 35%,#e8e9ec 60%,#b9b3aa 100%)}
.hero h1{position:absolute;left:84px;top:200px;font-family:"Cinzel",Georgia,serif;font-weight:400;font-size:58px;line-height:68px;color:#111;letter-spacing:1px}

/* intro */
.intro{height:340px;display:flex;gap:28px;padding:52px 82px 0 78px}
.intro-card{flex:1;height:233px;background:#f4f4f4;border:1px solid var(--line);display:flex;padding:14px;gap:16px}
.intro-card .photo{width:220px;height:205px;flex:none}
.intro-card h2{font-family:"Cinzel",Georgia,serif;font-weight:400;font-size:30px;line-height:32px;color:#222}
.intro-card h2 span{color:var(--blue)}
.intro-card p{font-size:12px;line-height:18px;color:var(--muted);margin:6px 0 12px}
.btn{display:inline-block;background:var(--blue);color:var(--white);font-family:"Cinzel",Georgia,serif;font-size:13px;padding:6px 12px;text-decoration:none}

/* practice */
.practice{height:573px;background:var(--blue-soft);position:relative}
.section-title{display:flex;align-items:center;gap:18px;font-family:"Cinzel",Georgia,serif;font-weight:400;font-size:30px;letter-spacing:1px}
.section-title::before,.section-title::after{content:"";flex:1;height:2px;background:currentColor;opacity:.6}
.practice .section-title{color:var(--white);position:absolute;left:80px;right:80px;top:42px}
.areas{position:absolute;left:81px;top:128px;display:flex;gap:28px}
.area{width:328px;height:445px;background:var(--blue);text-align:center;color:var(--white);position:relative}
.area::before{content:"";position:absolute;left:0;right:0;top:0;height:12px;border-top:3px solid rgba(255,255,255,.9)}
.area h3{font-family:"Cinzel",Georgia,serif;font-weight:400;font-size:19px;line-height:21px;margin-top:22px;color:#bfe7ff;display:flex;justify-content:center;gap:10px;align-items:flex-start}
.area p{font-size:12px;line-height:17px;padding:12px 24px 0}
.area p a{font-family:"Cinzel",Georgia,serif;color:#bfe7ff;text-decoration:none}
.area .photo{position:absolute;left:50px;right:50px;bottom:0;height:255px;background:linear-gradient(180deg,var(--blue) 0%,#2a2a30 55%,#1a1a1f 100%)}
.arrow{position:absolute;top:310px}
.arrow.left{left:26px}.arrow.right{right:26px}

/* about */
.about{height:679px;position:relative}
.about-text{position:absolute;left:78px;top:56px;width:678px}
.about-text h2{font-family:"Cinzel",Georgia,serif;font-weight:400;font-size:30px;display:flex;align-items:center;gap:10px;color:#222}
.about-text h2 span{color:var(--blue)}
.about-text h2::after{content:"";flex:1;height:2px;background:var(--blue-soft)}
.about-text .lead{font-style:italic;font-size:12px;line-height:18px;color:#444;margin-top:10px}
.about-text .photo{width:678px;height:380px;border:5px solid #fff;outline:1px solid #999;margin-top:22px;background:linear-gradient(90deg,#d9d7d2 0%,#cfc9bd 30%,#5f5a4f 48%,#3a362f 55%,#c8c4bb 72%,#e4e2dd 100%)}
.about-text .body{font-size:12px;line-height:18px;color:#444;margin-top:14px}

.help-form{position:absolute;left:791px;top:58px;width:328px;height:566px;background:var(--panel);color:var(--white)}
.help-head{background:var(--blue);height:82px;text-align:center;padding-top:10px;clip-path:polygon(0 0,100% 0,100% 78%,50% 100%,0 78%)}
.help-head h3{font-family:"Cinzel",Georgia,serif;font-weight:400;font-size:22px;line-height:26px}
.help-head small{font-family:"Cinzel",Georgia,serif;font-size:11px;color:#bfe7ff}
.help-form form{padding:18px 40px 0}
.help-form label{display:block;font-size:12px;margin-top:6px}
.field{height:34px;background:#fff;margin:4px 0 12px;display:flex;align-items:center;padding-left:8px}
.field.tall{height:124px;align-items:flex-start;padding-top:6px}
.submit{display:block;width:100%;height:38px;background:var(--blue);border:0;color:#fff;font-family:"Cinzel",Georgia,serif;font-size:16px;margin-top:12px}

/* cases */
.cases{height:533px;position:relative;background:linear-gradient(100deg,#d5d2cb 0%,#bfb9ad 40%,#6a6a66 60%,#8b7f6c 100%)}
.cases-panel{position:absolute;left:78px;top:0;width:331px;height:533px;background:rgba(40,40,42,.94);color:#fff;padding:18px 24px}
.cases-panel h2{font-family:"Cinzel",Georgia,serif;font-weight:400;font-size:24px;white-space:nowrap;border-bottom:2px solid #fff;padding-bottom:8px}
.case{padding:22px 0 18px;border-bottom:1px dashed #8aa8ff}
.case:last-of-type{border-bottom:0}
.case h4{font-family:"Cinzel",Georgia,serif;font-weight:700;color:#9fd7ff;font-size:14px;margin-bottom:8px}
.case p{font-size:12px;line-height:17px;color:#ddd}
.cases-panel .btn{display:block;text-align:center;font-size:18px;padding:8px;margin-top:8px;white-space:nowrap}

/* testimonials */
.testimonials{height:390px;position:relative}
.testimonials .section-title{color:var(--blue);position:absolute;left:80px;right:80px;top:42px}
.quotes{position:absolute;left:88px;top:127px;display:flex;gap:52px}
.quote{height:141px;border:2px solid #333;border-radius:4px;padding:18px 22px;position:relative;background:#fff}
.quote:first-child{width:478px}.quote:last-child{width:489px}
.quote::before{content:"\201C";position:absolute;left:12px;top:-4px;font-size:110px;color:#d4e4ff;font-family:Georgia,serif;line-height:1}
.quote p{position:relative;font-size:12px;line-height:17px;color:#333;padding-right:10px}
.quote cite{position:relative;display:block;margin-top:18px;font-family:"Cinzel",Georgia,serif;font-style:normal;color:var(--blue);font-size:15px}
.avatar{position:absolute;right:28px;bottom:-48px;width:100px;height:100px;border-radius:50%;border:4px solid #c0202a;background:radial-gradient(circle at 50% 40%,#c8ccd6,#6f7786)}

/* footer */
.site-footer{height:334px;background:var(--footer);color:#ddd;position:relative}
.f-col{position:absolute;top:30px}
.f-col h4{font-family:"Cinzel",Georgia,serif;font-weight:400;font-size:17px;color:var(--cyan);margin-bottom:20px}
.news{left:80px;width:440px}
.news-item{display:flex;gap:18px;margin-bottom:20px}
.news-item .photo{width:108px;height:68px;flex:none;background:linear-gradient(180deg,#e8e8ea,#555a66)}
.news-item h5{font-weight:400;font-size:13px;color:#7fa9ff}
.news-item time{display:block;font-size:11px;color:#fff;font-weight:600;margin:2px 0 6px}
.news-item p{font-size:11px;line-height:15px;color:#bbb}
.f-div{position:absolute;top:30px;width:1px;height:250px;background:#3a3a3a}
.info{left:633px}
.info ul{list-style:none;font-size:13px;line-height:18px}
.info li{display:flex;gap:14px;margin-bottom:14px}
.info svg{flex:none;margin-top:2px}
.follow{left:1020px}
.follow ul{list-style:none;font-size:12px}
.follow li{display:flex;align-items:center;gap:10px;margin-bottom:11px}
.follow .sq{width:24px;height:24px;background:var(--blue-soft);border-radius:3px}
.footer-bar{position:absolute;left:0;right:0;bottom:0;height:29px;background:var(--footer-bar);font-family:"Cinzel",Georgia,serif;font-size:12px;color:#9fd7ff;display:flex;align-items:center;justify-content:space-between;padding:0 80px}
.footer-bar nav a{color:#9fd7ff;text-decoration:none;padding:0 12px}
.footer-bar nav a+a{border-left:1px solid #9fd7ff}
</style>
</head>
<body>

<header class="site-header">
  <div class="brand">
    <div class="brand-name">MERCIECA &amp; BORG</div>
    <div class="brand-tag">ADVOCATES</div>
  </div>
  <div class="contact-col c1">
    <div class="row">
      <svg width="14" height="14" viewBox="0 0 24 24"><path fill="#0d47ec" d="M6.6 10.8a15 15 0 0 0 6.6 6.6l2.2-2.2c.3-.3.7-.4 1-.2 1.1.4 2.3.6 3.6.6.6 0 1 .4 1 1V20c0 .6-.4 1-1 1A17 17 0 0 1 3 4c0-.6.4-1 1-1h3.5c.6 0 1 .4 1 1 0 1.3.2 2.5.6 3.6.1.3 0 .7-.2 1z"/></svg>
      <div>(356) 2000 1101 (Valletta) /<br>(356) 2000 1102 (Birkirkara)</div>
    </div>
    <div class="row">
      <svg width="14" height="12" viewBox="0 0 24 18"><rect width="24" height="18" rx="2" fill="#0d47ec"/><path d="M2 2l10 8 10-8" stroke="#fff" stroke-width="2" fill="none"/></svg>
      <div>info@mbadvocates.example</div>
    </div>
  </div>
  <div class="contact-col c2">
    <div class="row">
      <svg width="12" height="16" viewBox="0 0 24 32"><path fill="#0d47ec" d="M12 0a12 12 0 0 0-12 12c0 9 12 20 12 20s12-11 12-20A12 12 0 0 0 12 0zm0 17a5 5 0 1 1 0-10 5 5 0 0 1 0 10z"/></svg>
      <div>12/4, Lantern Street, Valletta<br>88, Orchard Street, Birkirkara</div>
    </div>
    <div class="row">
      <svg width="14" height="14" viewBox="0 0 24 24"><rect x="2" y="8" width="20" height="14" rx="2" fill="#0d47ec"/><rect x="6" y="2" width="12" height="8" fill="#0d47ec"/></svg>
      <div>(356) 2000 1103</div>
    </div>
  </div>
</header>

<nav class="main-nav">
  <a href="#">Home</a><a href="#">About Us</a><a href="#">Practice Areas</a><a href="#">About Malta</a><a href="#">News &amp; Blog</a><a href="#">Contact</a>
</nav>

<section class="hero" role="img" aria-label="Lawyer signing documents at a desk beside a bronze statue of Lady Justice">
  <h1>FORCEFUL ADVOCACY,<br>TRUSTED ADVICE</h1>
</section>

<section class="intro">
  <article class="intro-card">
    <div class="photo" role="img" aria-label="Team of smiling lawyers in business suits" style="background:linear-gradient(180deg,#cfd8e4,#3a3f4a)"></div>
    <div>
      <h2>OUR <span>FIRM</span></h2>
      <p>Lorem ipsum dolor sit amet, consectetur adipiscing elit. Duis et nisi laoreet, rutrum magna vitae, suscipit sem. Morbi dignissim maximus mollis. Praesent eget tincidunt arcu. Nulla ut ipsum luctus, lobortis felis non, molestie lorem. Suspendisse pulvinar felis id lacinia pellentesque.</p>
      <a class="btn" href="#">READ MORE</a>
    </div>
  </article>
  <article class="intro-card">
    <div class="photo" role="img" aria-label="Law books and a gavel on a desk" style="background:linear-gradient(160deg,#e6ddd0,#7a5a3e)"></div>
    <div>
      <h2>OUR <span>VALUES</span></h2>
      <p>Lorem ipsum dolor sit amet, consectetur adipiscing elit. Duis et nisi laoreet, rutrum magna vitae, suscipit sem. Morbi dignissim maximus mollis. Praesent eget tincidunt arcu. Nulla ut ipsum luctus, lobortis felis non, molestie lorem. Suspendisse pulvinar felis id lacinia pellentesque.</p>
      <a class="btn" href="#">READ MORE</a>
    </div>
  </article>
</section>

<section class="practice">
  <h2 class="section-title">OUR PRACTISE AREAS</h2>
  <svg class="arrow left" width="16" height="40" viewBox="0 0 16 40"><path d="M14 2L2 20l12 18" stroke="#fff" stroke-width="2" fill="none"/></svg>
  <svg class="arrow right" width="16" height="40" viewBox="0 0 16 40"><path d="M2 2l12 18L2 38" stroke="#fff" stroke-width="2" fill="none"/></svg>
  <div class="areas">
    <article class="area">
      <h3><svg width="28" height="20" viewBox="0 0 28 20"><circle cx="7" cy="12" r="5.5" stroke="#fff" stroke-width="2" fill="none"/><circle cx="21" cy="12" r="5.5" stroke="#fff" stroke-width="2" fill="none"/><path d="M12 10h4" stroke="#fff" stroke-width="2"/></svg><span>CRIMINAL<br>LAW</span></h3>
      <p>Integer eget lectus sodales, porta eros vel, . Sed commodo .Phasellus vehicula orci erat, nisi commodo quis. <a href="#">READ MORE...</a></p>
      <div class="photo" role="img" aria-label="Lawyer in a dark suit standing with hands crossed"></div>
    </article>
    <article class="area">
      <h3><svg width="22" height="22" viewBox="0 0 22 22"><circle cx="8" cy="6" r="4" fill="#fff"/><path d="M1 20c0-5 3-8 7-8s7 3 7 8z" fill="#fff"/><circle cx="17" cy="16" r="4" fill="#bfe7ff"/></svg><span>OVERSEAS PATRON<br>SCHEME LAW</span></h3>
      <p>Integer eget lectus sodales, porta eros vel, . Sed commodo .Phasellus vehicula orci erat, nisi commodo quis. <a href="#">READ MORE...</a></p>
      <div class="photo" role="img" aria-label="Two investors holding a savings jar and a bank card"></div>
    </article>
    <article class="area">
      <h3><svg width="22" height="22" viewBox="0 0 22 22"><rect x="1" y="12" width="5" height="9" fill="#fff"/><rect x="8" y="7" width="5" height="14" fill="#fff"/><rect x="15" y="2" width="5" height="19" fill="#fff"/></svg><span>COMMERCIAL AND<br>CORPORATE LAW</span></h3>
      <p>Integer eget lectus sodales, porta eros vel, . Sed commodo .Phasellus vehicula orci erat, nisi commodo quis. <a href="#">READ MORE...</a></p>
      <div class="photo" role="img" aria-label="Two business lawyers standing with arms folded"></div>
    </article>
  </div>
</section>

<section class="about">
  <div class="about-text">
    <h2>ABOUT <span>US</span></h2>
    <p class="lead">Sed id ante at ex blandit congue ac eget erat. Sed lacinia, dui id molestie facilisis, enim sem tempus ligula, sed fringilla arcu nisi non tellus. Sed porta et nibh porttitor condimentum. Mauris congue semper accumsan.</p>
    <div class="photo" role="img" aria-label="Two lawyers shaking hands between stone columns at a courthouse entrance"></div>
    <p class="body">Fusce molestie tortor sed enim malesuada porttitor. Maecenas consectetur posuere ullamcorper. Nunc malesuada molestie finibus. Curabitur non vulputate est. Etiam sed leo lacinia, consectetur orci tempor, vulputate augue. Fusce elit nulla, blandit ultrices lobortis ac, porttitor eget odio.</p>
  </div>
  <aside class="help-form">
    <div class="help-head">
      <h3>HOW CAN WE HELP YOU?</h3>
      <small>TELL US ABOUT YOUR PROBLEM</small>
    </div>
    <form>
      <label>Name</label>
      <div class="field"><svg width="14" height="14" viewBox="0 0 24 24"><circle cx="12" cy="7" r="5" fill="#888"/><path d="M2 23c0-6 4-9 10-9s10 3 10 9z" fill="#888"/></svg></div>
      <label>Phone Number</label>
      <div class="field"><svg width="14" height="14" viewBox="0 0 24 24"><path fill="#888" d="M6.6 10.8a15 15 0 0 0 6.6 6.6l2.2-2.2c.3-.3.7-.4 1-.2 1.1.4 2.3.6 3.6.6.6 0 1 .4 1 1V20c0 .6-.4 1-1 1A17 17 0 0 1 3 4c0-.6.4-1 1-1h3.5c.6 0 1 .4 1 1 0 1.3.2 2.5.6 3.6.1.3 0 .7-.2 1z"/></svg></div>
      <label>Email Address</label>
      <div class="field" style="color:#888;font-size:15px">@</div>
      <label>Please Include Your Legal Issue</label>
      <div class="field tall"><svg width="18" height="14" viewBox="0 0 24 18"><path d="M2 1h14v9H8l-4 3v-3H2z" fill="#888"/><path d="M18 5h4v9h-2v3l-4-3h-6v-2h8z" fill="#888"/></svg></div>
      <button class="submit" type="button">SUBMIT</button>
    </form>
  </aside>
</section>

<section class="cases" role="img" aria-label="Lawyers reviewing a blue case file together at a meeting table">
  <div class="cases-panel">
    <h2>CASE SETTLEMENT</h2>
    <div class="case"><h4>Work Injury Case In Willington</h4><p>Nulla porttitor enim sit amet, eget laoreet odio lobortis eget. Maecenas non gravid nisl. Man etiam eleifend vehicula magna.</p></div>
    <div class="case"><h4>Work Injury Case In Willington</h4><p>Nulla porttitor enim sit amet, eget laoreet odio lobortis eget. Maecenas non gravid nisl. Man etiam eleifend vehicula magna.</p></div>
    <div class="case"><h4>Work Injury Case In Willington</h4><p>Nulla porttitor enim sit amet, eget laoreet odio lobortis eget. Maecenas non gravid nisl. Man etiam eleifend vehicula magna.</p></div>
    <a class="btn" href="#">View All Case Results</a>
  </div>
</section>

<section class="testimonials">
  <h2 class="section-title">TESTIMONIALS</h2>
  <div class="quotes">
    <blockquote class="quote">
      <p>Lorem ipsum dolor sit amet, consectetur adipiscing elit. Nulla fermentum dignissim risus eleifend sagittis. Integer turpis mi, hendrerit a leo eu, vestibulum dictum sem. Nullam egestas mauris in dui cursus, nec porta lectus tempus.</p>
      <cite>Karl Mifsud</cite>
      <div class="avatar" role="img" aria-label="Portrait of client Karl Mifsud"></div>
    </blockquote>
    <blockquote class="quote">
      <p>Lorem ipsum dolor sit amet, consectetur adipiscing elit. Nulla fermentum dignissim risus eleifend sagittis. Integer turpis mi, hendrerit a leo eu, vestibulum dictum sem. Nullam egestas mauris in dui cursus, nec porta lectus tempus.</p>
      <cite>Elena Farrugia</cite>
      <div class="avatar" role="img" aria-label="Portrait of client Elena Farrugia"></div>
    </blockquote>
  </div>
</section>

<footer class="site-footer">
  <div class="f-col news">
    <h4>LATEST NEWS</h4>
    <div class="news-item">
      <div class="photo" role="img" aria-label="Lawyer in a meeting"></div>
      <div><h5>Lorem ipsum dolor sit ame onsectetur</h5><time>2nd Jan, 2015</time><p>Mauris euismod elit mi, et feugiat ante elementum ut. econse vehicula elementum rutrum. Vestibulum consequat nunc tortor, nec lacinia enim.</p></div>
    </div>
    <div class="news-item">
      <div class="photo" role="img" aria-label="Lawyers shaking hands"></div>
      <div><h5>Lorem ipsum dolor sit ame onsectetur</h5><time>2nd Jan, 2015</time><p>Mauris euismod elit mi, et feugiat ante elementum ut. econse vehicula elementum rutrum. Vestibulum consequat nunc tortor, nec lacinia enim.</p></div>
    </div>
  </div>
  <div class="f-div" style="left:560px"></div>
  <div class="f-col info">
    <h4>CONTACT INFORMATION</h4>
    <ul>
      <li><svg width="12" height="16" viewBox="0 0 24 32"><path fill="#fff" d="M12 0a12 12 0 0 0-12 12c0 9 12 20 12 20s12-11 12-20A12 12 0 0 0 12 0zm0 17a5 5 0 1 1 0-10 5 5 0 0 1 0 10z"/></svg><span>12/4, Lantern Street, Valletta<br>88, Orchard Street, Birkirkara</span></li>
      <li><svg width="14" height="14" viewBox="0 0 24 24"><path fill="#fff" d="M6.6 10.8a15 15 0 0 0 6.6 6.6l2.2-2.2c.3-.3.7-.4 1-.2 1.1.4 2.3.6 3.6.6.6 0 1 .4 1 1V20c0 .6-.4 1-1 1A17 17 0 0 1 3 4c0-.6.4-1 1-1h3.5c.6 0 1 .4 1 1 0 1.3.2 2.5.6 3.6.1.3 0 .7-.2 1z"/></svg><span>(356) 2000 1101 (Valletta) /<br>(356) 2000 1102 (Birkirkara)</span></li>
      <li><svg width="14" height="14" viewBox="0 0 24 24"><rect x="2" y="8" width="20" height="14" rx="2" fill="#fff"/><rect x="6" y="2" width="12" height="8" fill="#fff"/></svg><span>(356) 2000 1103</span></li>
      <li><svg width="14" height="12" viewBox="0 0 24 18"><rect width="24" height="18" rx="2" fill="#fff"/><path d="M2 2l10 8 10-8" stroke="#1c1c1d" stroke-width="2" fill="none"/></svg><span>info@mbadvocates.example</span></li>
    </ul>
  </div>
  <div class="f-div" style="left:960px"></div>
  <div class="f-col follow">
    <h4>FOLLOW US</h4>
    <ul>
      <li><span class="sq"></span>Newsroom</li>
      <li><span class="sq"></span>Network</li>
      <li><span class="sq"></span>Updates</li>
      <li><span class="sq"></span>Email</li>
    </ul>
  </div>
  <div class="footer-bar">
    <span>Copyright 2016 MB Advocates Law Firm. All Rights Are Reserved.</span>
    <nav><a href="#">Terms &amp; Privacy Statement</a><a href="#">Sitemap</a></nav>
  </div>
</footer>

</body>
</html>
```